Print Ad Design - Make An Accountant Look Interesting!

My firm is sponsoring a Business Innovation speaker series and we need to place an ad in the print brochure that will be distributed to all attendees at the 4 upcoming events.

The ad should be eye-catching, bold and clean. The size requirements are 4.5" wide by 6.5" tall. Please incorporate Darren's picture in the ad - feel free to either go with our corporate colours (black, white and teal - see logo and design element attached), or use completely different colours that stand out.

The following text should be used:

"Could you pay $30,000 less tax next year?

Darren Holcombe, Partner at KVTW Chartered Accountants, can show you how in his seminar and panel presentations.

www.kvtw-example.ca
The Go-To Accounting Firm For Entrepreneurs"

Target Market(s)

Owners, CEOs and Presidents of small and mid-sized privately-held companies with annual revenues ranging from $2M to $150M.

Industry/Entity Type

Business

Requirements
Must have
• 4.5" wide by 6.5" tall
Font should be Gill Sans MT
Final version must be in high-res JPEG file.
Should not have
• No clip art photos of fake accountants!
No American dollar bills (we are a Canadian firm!)
Please try to avoid overly-traditional/corporate designs.

```html
<!DOCTYPE html>
<html lang="en">
<head>
<meta charset="utf-8">
<title>Darren Holcombe – KVTW Chartered Accountants</title>
<link rel="stylesheet" href="https://fonts.googleapis.com/css2?family=Lato:ital,wght@0,700;0,900;1,700&display=swap">
<style>
  :root {
    --teal-deep: #0a8a97;
    --teal-mid: #3fa9b4;
    --teal-glow: #a8dde2;
    --dome-outer: #9fd3d9;
    --dome-inner: #b9e2e6;
    --ink: #0b0b0b;
    --page-edge: #e9e9e9;
    --portrait-light: #d2d2d2;
    --portrait-dark: #6a6a6a;
  }
  html, body {
    margin: 0;
    padding: 0;
    overflow: hidden;
    background: #ffffff;
  }
  .ad {
    position: relative;
    width: 847px;
    height: 1200px;
    overflow: hidden;
    background: radial-gradient(ellipse 62% 48% at 50% 58%, var(--teal-glow) 0%, var(--teal-mid) 55%, var(--teal-deep) 100%);
    font-family: "Lato", "Helvetica Neue", Arial, sans-serif;
    color: var(--ink);
  }
  .ad__domes {
    position: absolute;
    inset: 0;
  }
  .headline {
    position: absolute;
    top: 48px;
    left: 0;
    width: 100%;
    margin: 0;
    text-align: center;
    font-weight: 900;
    font-size: 56px;
    line-height: 78px;
    letter-spacing: 0.5px;
  }
  .portrait-stack {
    position: absolute;
    left: 244px;
    top: 268px;
    width: 318px;
    height: 456px;
  }
  .portrait-stack__page {
    position: absolute;
    width: 296px;
    height: 436px;
    background: var(--page-edge);
    border: 1px solid #bdbdbd;
  }
  .portrait-stack__page--back { left: 0; top: 0; }
  .portrait-stack__page--mid { left: 6px; top: 6px; }
  .portrait {
    position: absolute;
    left: 18px;
    top: 16px;
    width: 296px;
    height: 436px;
    background: linear-gradient(160deg, var(--portrait-light) 0%, #a4a4a4 45%, var(--portrait-dark) 100%);
    box-shadow: 6px 8px 10px rgba(0,0,0,0.35);
  }
  .speaker {
    position: absolute;
    left: 74px;
    top: 780px;
    margin: 0;
    font-weight: 900;
    font-size: 41px;
  }
  .speaker__role {
    position: absolute;
    left: 74px;
    top: 862px;
    margin: 0;
    font-weight: 700;
    font-size: 28px;
  }
  .speaker__pitch {
    position: absolute;
    left: 397px;
    top: 922px;
    margin: 0;
    font-style: italic;
    font-weight: 700;
    font-size: 29px;
    line-height: 48px;
  }
  .footer {
    position: absolute;
    left: 66px;
    top: 1104px;
    margin: 0;
    font-weight: 900;
    font-size: 18px;
    line-height: 25px;
  }
</style>
</head>
<body>
  <main class="ad">
    <svg class="ad__domes" width="847" height="1200" viewBox="0 0 847 1200" aria-hidden="true">
      <circle cx="500" cy="1360" r="720" fill="var(--dome-outer)" opacity="0.75"/>
      <circle cx="560" cy="1440" r="650" fill="var(--dome-inner)" opacity="0.8"/>
    </svg>

    <h1 class="headline">Could you pay<br>$30,000 less tax next year?</h1>

    <div class="portrait-stack">
      <div class="portrait-stack__page portrait-stack__page--back"></div>
      <div class="portrait-stack__page portrait-stack__page--mid"></div>
      <div class="portrait" role="img" aria-label="Black and white headshot of Darren Holcombe in a dark suit and striped tie"></div>
    </div>

    <h2 class="speaker">Darren Holcombe,</h2>
    <p class="speaker__role">Partner at KVTW Chartered Accountants,</p>
    <p class="speaker__pitch">can show you<br>how in his seminar<br>and panel presentations.</p>

    <p class="footer">www.kvtw-example.ca<br>The Go-To Accounting Firm For Entrepreneurs"</p>
  </main>
</body>
</html>
```